I need 2- Sided Tri-Fold Brochure Design for Social Media Marketing Sevices.

Here's the Website URL link: http://www.harborlane4.example/social-media-1/
The brochure should be similar to the site, but it also needs to be very eye-catching as well as professional

I'm looking a very Creative Designer to provide a very unique brochure that will equal sales..

File Type: PSD

Contact me if you have questions

```html
<!DOCTYPE html>
<html lang="en">
<head>
<meta charset="utf-8">
<title>Harbor Lane 4 – Social Media Tri-Fold Brochure</title>
<link href="https://fonts.googleapis.com/css2?family=Open+Sans:wght@400;600;700;800&display=swap" rel="stylesheet">
<style>
:root{
  --stage:#c6c6c6;
  --blue:#1f7cc1;
  --blue-dark:#15609e;
  --sky-top:#b9d6ee;
  --sky-mid:#dcebf7;
  --sky-low:#f3f8fc;
  --white:#ffffff;
  --ink:#2a4d6e;
  --green:#3fae49;
  --red:#e0454e;
  --purple:#7d5bb0;
  --purple-soft:#dcd3ee;
  --lime:#8cc63f;
  --lime-soft:#e2f0cf;
  --orange:#f39a2c;
  --orange-soft:#fde0c1;
  --gold:#d9a62a;
}
*{box-sizing:border-box;margin:0;padding:0}
html,body{width:1200px;height:4000px;overflow:hidden}
body{background:var(--stage);font-family:"Open Sans",Arial,sans-serif;color:var(--ink);position:relative}

.spread{position:absolute;left:50px;width:1100px;height:850px;display:grid;grid-template-columns:repeat(3,1fr);
  background:linear-gradient(180deg,var(--sky-top) 0%,var(--sky-mid) 45%,var(--sky-low) 100%);
  box-shadow:0 6px 18px rgba(0,0,0,.18)}
.spread--outside{top:1000px}
.spread--inside{top:2150px}
.panel{position:relative;overflow:hidden;border-right:1px solid rgba(31,124,193,.12)}
.panel:last-child{border-right:none}

/* bubble decoration bands */
.bubble-band{position:absolute;left:0;right:0;height:120px;
  background:linear-gradient(90deg,rgba(125,91,176,.35),rgba(31,124,193,.30),rgba(224,69,78,.28),rgba(90,190,230,.32));}
.bubble-band--top{top:0}
.bubble-band--bottom{bottom:0}

/* reasons panel */
.reasons{position:absolute;left:28px;right:28px;top:150px;bottom:30px;background:var(--blue);color:var(--white);padding:26px 24px}
.reasons__title{font-size:36px;font-weight:700;line-height:1;text-transform:uppercase}
.reasons__sub{font-size:21px;font-weight:600;text-transform:uppercase;margin-top:4px;margin-bottom:22px}
.reasons__item{font-size:12px;line-height:1.45;margin-bottom:15px;color:#e6f1fb}

/* middle outside panel */
.brand{display:flex;align-items:center;gap:8px;font-weight:800;color:var(--blue);font-size:27px}
.brand__dot{width:16px;height:16px;border-radius:50%;background:var(--blue)}
.middle__brand{position:absolute;top:150px;left:40px}
.middle__body{position:absolute;top:205px;left:40px;right:32px}
.middle__title{font-size:30px;font-weight:700;color:var(--blue);text-transform:uppercase;margin-bottom:14px}
.middle__line{font-size:13.5px;line-height:1.45;color:var(--blue-dark);margin-bottom:12px}
.badges{display:flex;gap:16px;align-items:center;margin:20px 0 18px 40px}
.badge-square{width:82px;height:96px;background:#f0e9c8;border:2px solid var(--gold)}
.badge-seal{width:62px;height:62px;border-radius:50%;background:#2c4f8f;margin-top:60px}
.middle__cta{font-size:15px;font-weight:700;color:var(--blue);line-height:1.3;margin-bottom:14px}
.middle__contact{font-size:12px;line-height:1.45;color:var(--blue-dark)}
.middle__contact strong{font-weight:700}

/* cover panel */
.cover__callout{position:absolute;top:0;left:0;width:100%;height:420px}
.cover__text{position:absolute;top:36px;left:20px;right:20px;text-align:center;color:var(--white)}
.cover__headline{font-size:23px;font-weight:600;line-height:1.3;text-transform:uppercase}
.cover__tagline{font-size:22px;font-weight:600;line-height:1.3;margin-top:30px}
.guarantee{position:absolute;top:430px;left:50%;transform:translateX(-50%);width:118px;height:118px;border-radius:50%;
  border:12px solid var(--green);background:var(--white);display:flex;flex-direction:column;align-items:center;justify-content:center;
  color:var(--blue-dark);text-align:center;line-height:1}
.guarantee__a{font-size:13px;font-weight:700}
.guarantee__b{font-size:26px;font-weight:800;color:var(--blue)}
.guarantee__c{font-size:8.5px;font-weight:700}
.cover__cluster{position:absolute;top:555px;left:40px;right:40px;height:120px;border-radius:60px;
  background:radial-gradient(ellipse at center,rgba(125,91,176,.45),rgba(31,124,193,.35) 50%,rgba(224,69,78,.15) 85%,transparent)}
.cover__brand{position:absolute;top:690px;left:0;right:0;text-align:center}
.cover__brand .brand{justify-content:center;font-size:29px}
.cover__slogan{font-size:12px;color:var(--blue-dark);margin-top:2px}
.callbar{position:absolute;left:0;right:0;bottom:0;height:56px;background:var(--blue);color:var(--white);
  font-size:22px;font-weight:700;display:flex;align-items:center;justify-content:center}

/* inside packages */
.pkg{position:absolute;top:140px;bottom:150px;left:28px;right:28px}
.pkg__label{font-size:13px;font-weight:700;color:var(--blue-dark);text-transform:uppercase;margin-bottom:6px}
.pkg__card{border-radius:14px;overflow:hidden;height:calc(100% - 24px);box-shadow:0 3px 8px rgba(0,0,0,.12)}
.pkg__price{color:var(--white);font-size:24px;font-weight:700;text-align:center;padding:10px 0}
.pkg__body{padding:14px 16px;font-size:11.5px;line-height:1.4;height:100%}
.pkg__body p{margin-bottom:8px}
.pkg__body b{font-weight:700;color:var(--blue-dark)}
.pkg__note{font-size:10px;font-style:italic}
.pkg__list-title{font-size:13px;font-weight:700;text-transform:uppercase;margin:10px 0 6px}
.pkg__list{list-style:none;font-size:10.5px}
.pkg__list li{margin-bottom:5px}
.pkg--basic .pkg__price{background:var(--purple)} .pkg--basic .pkg__body{background:var(--purple-soft)} .pkg--basic .pkg__list-title{color:var(--purple)}
.pkg--deluxe .pkg__price{background:var(--lime)} .pkg--deluxe .pkg__body{background:var(--lime-soft)} .pkg--deluxe .pkg__list-title{color:#5d9a1f}
.pkg--leaders .pkg__price{background:var(--orange)} .pkg--leaders .pkg__body{background:var(--orange-soft)} .pkg--leaders .pkg__list-title{color:#d9791a}
</style>
</head>
<body>

<!-- Outside of the brochure -->
<section class="spread spread--outside">
  <div class="panel panel--reasons">
    <div class="bubble-band bubble-band--top" role="img" aria-label="Row of colourful social network speech bubbles"></div>
    <div class="reasons">
      <h2 class="reasons__title">7 Reasons</h2>
      <p class="reasons__sub">Businesses Need</p>
      <p class="reasons__item">82% of customers feel more comfortable buying from a company with a strong Social Media presence</p>
      <p class="reasons__item">91% of businesses would trust recommending another business when they are actively involved online</p>
      <p class="reasons__item">78% of businesses increased online sells by 56% using Videos, Pictures and Content Optimization</p>
      <p class="reasons__item">83% of customers would click on a LINK if the business had over 20,000 FriendPage LIKES and 100,000 Chirper Followers</p>
      <p class="reasons__item">89% of social media sites can attract millions of targeted clients around the world to your businesses</p>
      <p class="reasons__item">96% of marketer state that Social Media caused a 47% increase in their website traffic.</p>
      <p class="reasons__item">85% of loyal fans supported a business solely because of the large volume of people already supporting them</p>
    </div>
  </div>

  <div class="panel panel--middle">
    <div class="bubble-band bubble-band--top" role="img" aria-label="Row of colourful social network speech bubbles"></div>
    <div class="middle__brand brand"><span class="brand__dot"></span>Harbor Lane 4</div>
    <div class="middle__body">
      <h2 class="middle__title">Do You Have....</h2>
      <p class="middle__line">* 1/2 Million customers that FOLLOW you on Chirper....?</p>
      <p class="middle__line">* 1 Million / 40,000 / 1 Million customers that LIKE you on FriendPage...?</p>
      <p class="middle__line">* 1 Million customers that VIEW your videos on ClipStream...?</p>
      <p class="middle__line">WE DO....</p>
      <p class="middle__line">....And we can get MORE customers for your Business to.</p>
      <div class="badges">
        <div class="badge-square" role="img" aria-label="Money back guarantee badge"></div>
        <div class="badge-seal" role="img" aria-label="Quality seal"></div>
      </div>
      <p class="middle__cta">Contact us today to get<br>MORE Customers</p>
      <p class="middle__contact"><strong>Harbor Lane 4 Inc.</strong><br>
        Phone: (555) 014-2290<br>
        Email: resources@harborlane4.example<br>
        http://www.harborlane4.example/social-media-1/</p>
    </div>
  </div>

  <div class="panel panel--cover">
    <svg class="cover__callout" viewBox="0 0 367 420" preserveAspectRatio="none" aria-hidden="true">
      <path d="M0 0H367V345H140L95 400L100 345H0Z" fill="#1f7cc1"/>
    </svg>
    <div class="cover__text">
      <p class="cover__headline">We will increase your followers and turn them into customers</p>
      <p class="cover__tagline">Contact us Only if You Want A Stronger Online Presence</p>
    </div>
    <div class="guarantee"><span class="guarantee__a">RESULTS</span><span class="guarantee__b">100%</span><span class="guarantee__c">GUARANTEED</span></div>
    <div class="cover__cluster" role="img" aria-label="Cluster of colourful social network speech bubbles"></div>
    <div class="cover__brand">
      <div class="brand"><span class="brand__dot"></span>Harbor Lane 4</div>
      <p class="cover__slogan">Taking your brand to the next lane</p>
    </div>
    <div class="callbar">Call: (555) 014-2290</div>
  </div>
</section>

<!-- Inside of the brochure -->
<section class="spread spread--inside">
  <div class="panel">
    <div class="bubble-band bubble-band--top" role="img" aria-label="Row of colourful social network speech bubbles"></div>
    <div class="pkg pkg--basic">
      <p class="pkg__label">3 Month "Basic" SEO Package</p>
      <div class="pkg__card">
        <div class="pkg__price">$225 (a month)</div>
        <div class="pkg__body">
          <p><b>INCLUDES:</b> 40,000 (Chirper Followers)</p>
          <p><b>INCLUDES:</b> 1300 (FriendPage Fan Page Likes)</p>
          <p><b>INCLUDES:</b> 25,000 (ClipStream Views)</p>
          <p><b>INCLUDES:</b> Re-share any message 1 time every month for 3 months to our One Million Chirper Followers</p>
          <p><b>INCLUDES:</b> Re-post any message 1 time every month for 3 months to our 40,000 FriendPage Fans</p>
          <p class="pkg__note">"We offer 100% Money Back Guarantee you will have all LIKES, FOLLOWERS &amp; VIEWS by the end of your 3 Month Campaign"</p>
          <p class="pkg__list-title">3 Months Package Includes</p>
          <ol class="pkg__list">
            <li>1. Assigned to 3 Person Marketing Team</li>
            <li>2. Setup and Design (FriendPage, Chirper &amp; ClipStream) Pages</li>
            <li>3. Monitor and Engage Online Community</li>
            <li>4. All Social Media Sites Linked Together</li>
            <li>5. Develop and Implement Target Marketing Strategies</li>
            <li>6. Campaign Manager Finalization Review</li>
          </ol>
        </div>
      </div>
    </div>
    <div class="bubble-band bubble-band--bottom" role="img" aria-label="Row of colourful social network speech bubbles"></div>
  </div>

  <div class="panel">
    <div class="bubble-band bubble-band--top" role="img" aria-label="Row of colourful social network speech bubbles"></div>
    <div class="pkg pkg--deluxe">
      <p class="pkg__label">6 Month "Deluxe" SEO Package</p>
      <div class="pkg__card">
        <div class="pkg__price">$400 (a month)</div>
        <div class="pkg__body">
          <p><b>INCLUDES:</b> 125,000 (Chirper Followers)</p>
          <p><b>INCLUDES:</b> 7,000 (FriendPage Fan Page Likes)</p>
          <p><b>INCLUDES:</b> 100,000 (ClipStream Views)</p>
          <p><b>INCLUDES:</b> Re-share any message 3 times every month for 3 months to our One Million Chirper Followers</p>
          <p><b>INCLUDES:</b> Re-post any message 3 times every month for 3 months to our 40,000 FriendPage Fans</p>
          <p class="pkg__note">"We offer 100% Money Back Guarantee you will have all LIKES, FOLLOWERS &amp; VIEWS by the end of your 6 Month Campaign"</p>
          <p class="pkg__list-title">6 Months Package Includes</p>
          <ol class="pkg__list">
            <li>1. Assigned to 3 Person Marketing Team</li>
            <li>2. Setup and Design (FriendPage, Chirper &amp; ClipStream) Pages</li>
            <li>3. Monitor and Engage Online Community</li>
            <li>4. All Social Media Sites Linked Together</li>
            <li>5. Develop and Implement Target Marketing Strategies</li>
            <li>6. Campaign Manager Finalization Review</li>
          </ol>
        </div>
      </div>
    </div>
    <div class="bubble-band bubble-band--bottom" role="img" aria-label="Row of colourful social network speech bubbles"></div>
  </div>

  <div class="panel">
    <div class="bubble-band bubble-band--top" role="img" aria-label="Row of colourful social network speech bubbles"></div>
    <div class="pkg pkg--leaders">
      <p class="pkg__label">9 Month "Leaders" SEO Package</p>
      <div class="pkg__card">
        <div class="pkg__price">$670 (a month)</div>
        <div class="pkg__body">
          <p><b>INCLUDES:</b> 250,000 (Chirper Followers)</p>
          <p><b>INCLUDES:</b> 15,000 (FriendPage Fan Page Likes)</p>
          <p><b>INCLUDES:</b> 250,000 (ClipStream Views)</p>
          <p><b>INCLUDES:</b> Re-share any message 10 time every month for 3 months to our One Million Chirper Followers</p>
          <p><b>INCLUDES:</b> Re-post any message 10 time every month for 3 months to our 40,000 FriendPage Fans</p>
          <p class="pkg__note">"We offer 100% Money Back Guarantee you will have all LIKES, FOLLOWERS &amp; VIEWS by the end of your 9 Month Campaign"</p>
          <p class="pkg__list-title">9 Months Package Includes</p>
          <ol class="pkg__list">
            <li>1. Assigned to 5 Person Marketing Team</li>
            <li>2. Setup and Design (FriendPage, Chirper &amp; ClipStream) Pages</li>
            <li>3. Monitor and Engage Online Community</li>
            <li>4. All Social Media Sites Linked Together</li>
            <li>5. Develop and Implement Target Marketing Strategies</li>
            <li>6. Campaign Manager Finalization Review</li>
          </ol>
        </div>
      </div>
    </div>
    <div class="bubble-band bubble-band--bottom" role="img" aria-label="Row of colourful social network speech bubbles"></div>
  </div>
</section>

</body>
</html>
```